Update New Business Card - For Start Up

I need to update my business card, I have our old version for example. I would like to keep to the same colors and theme. We are a threat reporting and case management tool for corporations and educational institutions.

Target Market(s)

Corporate Security and Human Resources, School Administrators and Superintendents.

Industry/Entity Type

Physical Security and Technology.

Contact Information for Business Card

My Name, Founder/CEO, phone number 555-214-6082, Logo, Web...

Colors
0054AA
0677BA
7BADD7
CADEEF
E8F1F8

Requirements
Must have
• Something new and trendy.

```html
<!DOCTYPE html>
<html lang="en">
<head>
<meta charset="utf-8">
<title>Vantora Business Card</title>
<link href="https://fonts.googleapis.com/css2?family=Jost:wght@400;500;600&display=swap" rel="stylesheet">
<style>
  :root {
    --backdrop: #3b3b3b;
    --card-white: #ffffff;
    --card-tint: #f4f5f7;
    --navy: #2a3a9c;
    --royal: #1f4fb0;
    --blue: #0677ba;
    --ink: #111111;
    --white: #ffffff;
  }
  html, body {
    margin: 0;
    width: 1200px;
    height: 900px;
    overflow: hidden;
    background: var(--backdrop);
    font-family: "Jost", sans-serif;
  }
  .canvas {
    position: relative;
    width: 1200px;
    height: 900px;
  }
  .card {
    position: absolute;
    width: 668px;
    height: 381px;
    overflow: hidden;
  }
  .card-front {
    left: 275px;
    top: 51px;
    background: var(--card-white);
  }
  .card-back {
    left: 274px;
    top: 450px;
  }
  .card-texture {
    position: absolute;
    inset: 0;
  }
  .card-front .card-texture {
    background: var(--card-tint);
  }
  .card-back .card-texture {
    background: linear-gradient(90deg, var(--navy) 0%, #2456b0 55%, var(--blue) 100%);
  }
  .brand {
    position: absolute;
    display: flex;
    align-items: center;
  }
  .brand-dot {
    border-radius: 50%;
    flex: none;
  }
  .brand-name {
    font-weight: 500;
    letter-spacing: 0.14em;
    line-height: 1;
  }
  .card-front .brand {
    left: 152px;
    top: 60px;
    height: 76px;
  }
  .card-front .brand-dot {
    width: 72px;
    height: 72px;
    background: var(--royal);
    margin-right: 18px;
  }
  .card-front .brand-name {
    font-size: 38px;
    color: var(--royal);
  }
  .divider-band {
    position: absolute;
    left: 0;
    top: 171px;
    width: 100%;
    height: 7px;
    background: linear-gradient(90deg, var(--navy), var(--blue));
  }
  .holder {
    position: absolute;
    right: 339px;
    top: 236px;
    text-align: right;
  }
  .holder-name {
    margin: 0;
    font-size: 35px;
    font-weight: 600;
    color: var(--ink);
    line-height: 1;
  }
  .holder-title {
    margin: 6px 0 0;
    font-size: 14.5px;
    font-weight: 400;
    color: var(--navy);
    letter-spacing: 0.02em;
  }
  .contact-rule {
    position: absolute;
    left: 357px;
    top: 233px;
    width: 1px;
    height: 78px;
    background: var(--navy);
  }
  .contact-list {
    position: absolute;
    left: 373px;
    top: 234px;
    margin: 0;
    padding: 0;
    list-style: none;
  }
  .contact-list li {
    display: flex;
    align-items: center;
    height: 25px;
    font-size: 15px;
    color: var(--ink);
  }
  .contact-list svg {
    width: 14px;
    height: 14px;
    margin-right: 13px;
    fill: var(--navy);
    flex: none;
  }
  .card-back .brand {
    left: 140px;
    top: 144px;
    height: 84px;
  }
  .card-back .brand-dot {
    width: 84px;
    height: 84px;
    background: var(--white);
    margin-right: 16px;
  }
  .card-back .brand-name {
    font-size: 44px;
    color: var(--white);
  }
</style>
</head>
<body>
<div class="canvas">
  <section class="card card-front">
    <div class="card-texture" role="img" aria-label="Faint repeating brand pattern"></div>
    <div class="brand">
      <span class="brand-dot"></span>
      <span class="brand-name">VANTORA</span>
    </div>
    <div class="divider-band"></div>
    <div class="holder">
      <h1 class="holder-name">Owen Castellan</h1>
      <p class="holder-title">CHIEF EXECUTIVE OFFICER</p>
    </div>
    <div class="contact-rule"></div>
    <ul class="contact-list">
      <li>
        <svg viewBox="0 0 24 24"><path d="M6.6 10.8a15.1 15.1 0 0 0 6.6 6.6l2.2-2.2a1 1 0 0 1 1-.25 11.4 11.4 0 0 0 3.6.57 1 1 0 0 1 1 1V20a1 1 0 0 1-1 1A17 17 0 0 1 3 4a1 1 0 0 1 1-1h3.5a1 1 0 0 1 1 1c0 1.25.2 2.45.57 3.57a1 1 0 0 1-.25 1z"/></svg>
        888-899-3799 | 555-214-6082
      </li>
      <li>
        <svg viewBox="0 0 24 24"><path d="M2 5h20v2l-10 6L2 7z"/><path d="M2 9l10 6 10-6v10H2z"/></svg>
        owen@vantora.co
      </li>
      <li>
        <svg viewBox="0 0 24 24"><path d="M12 2a10 10 0 1 0 0 20 10 10 0 0 0 0-20zm6.9 6h-2.9a15.6 15.6 0 0 0-1.4-3.6A8 8 0 0 1 18.9 8zM12 4c.8 1.2 1.5 2.5 1.9 4h-3.8c.4-1.5 1.1-2.8 1.9-4zM4.3 14a8 8 0 0 1 0-4h3.4a16.5 16.5 0 0 0 0 4zm.8 2H8c.3 1.3.8 2.5 1.4 3.6A8 8 0 0 1 5.1 16zM8 8H5.1a8 8 0 0 1 4.3-3.6C8.8 5.5 8.3 6.7 8 8zm4 12c-.8-1.2-1.5-2.5-1.9-4h3.8c-.4 1.5-1.1 2.8-1.9 4zm2.3-6H9.7a14.7 14.7 0 0 1 0-4h4.6a14.7 14.7 0 0 1 0 4zm.3 5.6c.6-1.1 1.1-2.3 1.4-3.6h2.9a8 8 0 0 1-4.3 3.6zM16.3 14a16.5 16.5 0 0 0 0-4h3.4a8 8 0 0 1 0 4z"/></svg>
        www.vantora.com
      </li>
    </ul>
  </section>

  <section class="card card-back">
    <div class="card-texture" role="img" aria-label="Blue gradient with faint repeating brand pattern"></div>
    <div class="brand">
      <span class="brand-dot"></span>
      <span class="brand-name">VANTORA</span>
    </div>
  </section>
</div>
</body>
</html>
```